Bright Oak Fitness Facility Business Cards

Business Card Design that incorporates the logo and tagline

Target Market(s)

Fitness, People Who Exercise

Contact Information for Business Card

2817 Mossgrove Bend Road
Tavares, Florida 32190
Phone: 352-555-Jump (5867)
www.brightoakfitness.example
info@brightoakfitness.example

Requirements
Must have
• Logo, Address, Website, email and tagline "More Than A Gym". Colors should be red/black/grey/white

```html
<!DOCTYPE html>
<html lang="en">
<head>
<meta charset="utf-8">
<title>Bright Oak Fitness Facility – Business Card Options</title>
<link href="https://fonts.googleapis.com/css2?family=Ubuntu:wght@400;500&display=swap" rel="stylesheet">
<style>
  :root {
    --board: #8a0000;
    --card-grey: #575a5b;
    --brand-red: #d63440;
    --ink-black: #0b0b0b;
    --paper: #f9f9f9;
    --text-dark: #1c1c1c;
    --text-light: #ffffff;
  }
  html, body {
    margin: 0;
    padding: 0;
    width: 1200px;
    height: 1200px;
    overflow: hidden;
    background: var(--board);
    font-family: "Ubuntu", sans-serif;
  }
  .board {
    position: relative;
    width: 1200px;
    height: 1200px;
  }
  .option-number {
    position: absolute;
    font-family: "Ubuntu", sans-serif;
    font-size: 66px;
    line-height: 1;
    color: var(--ink-black);
  }
  .option-number--one { left: 122px; top: 92px; }
  .option-number--two { left: 1008px; top: 648px; }
  .card {
    position: absolute;
    width: 850px;
    height: 472px;
    box-shadow: 0 6px 18px rgba(0,0,0,0.45);
  }
  .card--front { left: 205px; top: 86px; }
  .card--alt { left: 113px; top: 649px; }
  .card svg { display: block; width: 100%; height: 100%; }
  .contact-text { font-family: "Ubuntu", sans-serif; font-size: 31px; fill: var(--text-dark); }
  .brand-name { font-family: "Ubuntu", sans-serif; font-weight: 500; font-size: 33px; fill: var(--brand-red); }
  .tagline { font-family: "Ubuntu", sans-serif; font-size: 37px; fill: var(--text-light); }
  .icon-ring { fill: none; stroke: var(--brand-red); stroke-width: 2.5; }
  .icon-glyph { fill: none; stroke: var(--brand-red); stroke-width: 2.2; stroke-linejoin: round; stroke-linecap: round; }
  .icon-solid { fill: var(--brand-red); }
  .edge-line { fill: none; stroke: #ffffff; stroke-width: 4; }
</style>
</head>
<body>
<main class="board">
  <div class="option-number option-number--one">1</div>
  <div class="option-number option-number--two">2</div>

  <svg width="0" height="0" style="position:absolute">
    <defs>
      <symbol id="icon-pin" viewBox="-24 -24 48 48">
        <circle class="icon-ring" r="22"/>
        <path class="icon-glyph" d="M0 10 C-8 1 -9 -3 -9 -6 A9 9 0 0 1 9 -6 C9 -3 8 1 0 10 Z"/>
        <circle class="icon-glyph" cy="-6" r="3.5"/>
        <path class="icon-glyph" d="M-12 8 C-14 14 14 14 12 8"/>
      </symbol>
      <symbol id="icon-phone" viewBox="-24 -24 48 48">
        <circle class="icon-ring" r="22"/>
        <path class="icon-solid" d="M-11 -12 L-5 -13 L-1 -5 L-5 -2 C-3 3 1 7 5 9 L8 5 L15 9 L14 14 C4 16 -14 2 -11 -12 Z"/>
      </symbol>
      <symbol id="icon-mail" viewBox="-24 -24 48 48">
        <circle class="icon-ring" r="22"/>
        <rect class="icon-solid" x="-12" y="-9" width="22" height="16" rx="2"/>
        <path d="M-12 -8 L-1 1 L10 -8" fill="none" stroke="#fff" stroke-width="2"/>
        <circle cx="10" cy="7" r="5" fill="#fff" stroke="var(--brand-red)" stroke-width="2"/>
      </symbol>
      <symbol id="icon-web" viewBox="-24 -24 48 48">
        <circle class="icon-ring" r="22"/>
        <circle class="icon-glyph" r="15"/>
        <ellipse class="icon-glyph" rx="7" ry="15"/>
        <line class="icon-glyph" x1="-15" y1="0" x2="15" y2="0"/>
        <rect x="-13" y="-4" width="26" height="8" fill="#fff" stroke="var(--brand-red)" stroke-width="1.8"/>
      </symbol>
    </defs>
  </svg>

  <!-- Option 1 -->
  <section class="card card--front" aria-label="Business card option 1">
    <svg viewBox="0 0 1063 590" xmlns="http://www.w3.org/2000/svg">
      <rect class="card-paper" width="1063" height="590" fill="var(--paper)"/>
      <polygon class="panel-grey" points="0,0 283,0 480,300 322,590 0,590" fill="var(--card-grey)"/>
      <polyline class="edge-line" points="283,0 480,300 322,590"/>
      <polygon class="stripe-red" points="290,0 382,0 522,300 484,256" fill="var(--brand-red)"/>
      <polygon class="stripe-black" points="382,0 442,0 474,184" fill="var(--ink-black)"/>
      <polygon class="stripe-red" points="484,258 522,302 344,590 328,590" fill="var(--brand-red)"/>
      <polygon class="stripe-black" points="510,332 346,590 412,590" fill="var(--ink-black)"/>

      <circle cx="214" cy="180" r="20" fill="var(--brand-red)"/>
      <text class="brand-name" x="214" y="268" text-anchor="middle" dominant-baseline="central">Bright Oak Fitness</text>
      <text class="tagline" x="220" y="383" text-anchor="middle" dominant-baseline="central">"More Than A Gym"</text>

      <use href="#icon-pin" x="495" y="97" width="48" height="48"/>
      <text class="contact-text" x="556" y="104" dominant-baseline="central">2817 Mossgrove Bend Road</text>
      <text class="contact-text" x="559" y="137" dominant-baseline="central">Tavares, Florida 32190</text>
      <use href="#icon-phone" x="536" y="210" width="48" height="48"/>
      <text class="contact-text" x="595" y="234" dominant-baseline="central">352-555-Jump (5867)</text>
      <use href="#icon-mail" x="538" y="324" width="48" height="48"/>
      <text class="contact-text" x="599" y="348" dominant-baseline="central">info@brightoakfitness.example</text>
      <use href="#icon-web" x="495" y="433" width="48" height="48"/>
      <text class="contact-text" x="557" y="457" dominant-baseline="central">www.brightoakfitness.example</text>
    </svg>
  </section>

  <!-- Option 2 -->
  <section class="card card--alt" aria-label="Business card option 2">
    <svg viewBox="0 0 1063 590" xmlns="http://www.w3.org/2000/svg">
      <rect class="card-grey" width="1063" height="590" fill="var(--card-grey)"/>
      <polygon class="panel-paper" points="14,154 77,18 709,18 759,99 484,572 14,572" fill="var(--paper)"/>
      <polygon class="stripe-red" points="80,18 122,18 17,170 17,150" fill="var(--brand-red)"/>
      <polygon class="stripe-black" points="122,18 180,18 17,192 17,170" fill="var(--ink-black)"/>
      <polygon class="stripe-black" points="707,18 724,18 799,106 502,572 484,572 759,99" fill="var(--ink-black)"/>
      <polygon class="stripe-red" points="724,18 762,18 899,104 519,572 502,572 799,106" fill="var(--brand-red)"/>
      <polyline class="edge-line" points="762,18 899,104 519,572"/>

      <circle cx="881" cy="292" r="20" fill="var(--brand-red)"/>
      <text class="brand-name" x="881" y="374" text-anchor="middle" dominant-baseline="central">Bright Oak Fitness</text>
      <text class="tagline" x="807" y="554" text-anchor="middle" dominant-baseline="central">"More Than A Gym"</text>

      <use href="#icon-pin" x="186" y="97" width="48" height="48"/>
      <text class="contact-text" x="247" y="104" dominant-baseline="central">2817 Mossgrove Bend Road</text>
      <text class="contact-text" x="250" y="137" dominant-baseline="central">Tavares, Florida 32190</text>
      <use href="#icon-phone" x="127" y="223" width="48" height="48"/>
      <text class="contact-text" x="186" y="248" dominant-baseline="central">352-555-Jump (5867)</text>
      <use href="#icon-mail" x="74" y="337" width="48" height="48"/>
      <text class="contact-text" x="135" y="361" dominant-baseline="central">info@brightoakfitness.example</text>
      <use href="#icon-web" x="32" y="446" width="48" height="48"/>
      <text class="contact-text" x="92" y="470" dominant-baseline="central">www.brightoakfitness.example</text>
    </svg>
  </section>
</main>
</body>
</html>
```